A resume/portfolio website for myself

I'm an independent software contractor, architect, tech trainer. I need a web site to present myself. Many ready to use portfolio designs are too artistic and focused on presenting design skills of the person. I like a nice website but the content should be a little less graphic than if you would present a graphic designer. Content could be presentation of me, core skill qualities and services and resume. Potentially a page with my tech courses in the longer run

```html
<!DOCTYPE html>
<html lang="en">
<head>
<meta charset="utf-8">
<title>Portfolio – Software Contractor, Architect &amp; Tech Trainer</title>
<link href="https://fonts.googleapis.com/css2?family=Montserrat:wght@400;500;600&display=swap" rel="stylesheet">
<style>
:root{
  --blue:#1572b0;
  --blue-soft:#8ab8d6;
  --band:#e2e4e9;
  --track:#cdd6e0;
  --panel:#cfd8e2;
  --field:#ececec;
  --ink:#2b2b2b;
  --muted:#444;
  --white:#fff;
}
*{box-sizing:border-box;margin:0;padding:0}
html,body{width:1200px;height:3460px;overflow:hidden;background:var(--white)}
body{font-family:'Montserrat',sans-serif;color:var(--ink);position:relative}
.abs{position:absolute}
p{font-size:15px;line-height:22.5px;color:var(--muted)}

/* nav */
.logo{left:149px;top:22px;font-size:22px;letter-spacing:.5px}
.nav{top:28px;left:0;width:1051px;font-size:14px}
.nav a{position:absolute;color:var(--ink);text-decoration:none;white-space:nowrap}

/* hero */
.hero-art{left:0;top:0}
.greeting{left:149px;top:216px;font-size:23px}
.headline{left:149px;top:254px;font-size:40px;font-weight:600;line-height:47px;width:560px}
.btn{display:flex;align-items:center;justify-content:center;font-size:14px;border-radius:2px;height:45px;width:151px;top:409px}
.btn-primary{left:149px;background:var(--blue);color:var(--white);font-weight:500}
.btn-outline{left:314px;border:2px solid var(--blue);color:var(--blue)}

/* bands */
.band{left:0;width:1200px;background:var(--band)}
.section-title{font-size:31px;font-weight:500;letter-spacing:.5px}
.section-title.center{left:0;width:1200px;text-align:center}
.rule{height:4px;background:var(--blue)}
.intro{left:0;width:1200px;text-align:center}

/* about */
.about-col{width:316px;font-size:15px}

/* services */
.card{top:1039px;width:285px;height:271px;background:var(--white);box-shadow:0 2px 8px rgba(0,0,0,.18);padding:28px 21px 0 21px}
.card svg{display:block;height:56px;margin-bottom:16px}
.card h3{font-size:19px;font-weight:500;margin-bottom:10px}
.card p{width:240px}

/* skills */
.skill{width:413px}
.skill-head{display:flex;justify-content:space-between;align-items:baseline;height:23px}
.skill-name{font-size:19px}
.skill-pct{font-size:14px}
.skill-track{margin-top:10px;height:20px;border-radius:10px;background:var(--track);overflow:hidden}
.skill-fill{height:100%;border-radius:10px;background:var(--blue)}

/* experience */
.timeline-line{left:603px;top:2140px;width:2px;height:418px;background:#e4ecf3}
.job-title{left:149px;width:300px;font-size:19px;line-height:28px}
.job-dot{left:593px;width:22px;height:22px;border:2.5px solid var(--blue);border-radius:50%;background:var(--white)}
.job-date{left:454px;width:300px;text-align:center;font-size:15px}
.job-text{left:774px;width:280px}

/* contact */
.contact-line{left:149px;display:flex;align-items:center;gap:18px;font-size:19px}
.contact-line svg{width:24px;height:24px}
.form-panel{left:450px;top:2764px;width:600px;height:469px;background:var(--panel)}
.label{font-size:19px}
.field{background:var(--field);border:1px solid #d8d8d8;font-size:14px;font-style:italic;color:#555;padding:0 15px;display:flex;align-items:center}
.submit{left:878px;top:3167px;width:150px;height:45px;background:var(--blue);color:var(--white);font-size:14px;font-weight:500;display:flex;align-items:center;justify-content:center;border-radius:2px}

/* footer */
.footer-rule{left:0;top:3293px;width:1200px;height:3px;background:var(--blue)}
.socials{left:0;top:3340px;width:1200px;display:flex;justify-content:center;gap:26px}
.social{display:flex;align-items:center;gap:7px;color:var(--blue);font-size:15px;font-weight:500}
.social i{width:18px;height:18px;border-radius:50%;background:var(--blue);display:block}
.copyright{left:0;top:3406px;width:1200px;text-align:center;font-size:15px}
</style>
</head>
<body>

<!-- header -->
<div class="abs logo">Logo</div>
<nav class="abs nav">
  <a style="left:503px">Home</a>
  <a style="left:591px">About</a>
  <a style="left:680px">Services</a>
  <a style="left:785px">Skills</a>
  <a style="left:867px">Experience</a>
  <a style="left:993px">Contact</a>
</nav>

<!-- hero -->
<svg class="abs hero-art" width="1200" height="600" viewBox="0 0 1200 600">
  <defs>
    <clipPath id="heroClip"><rect x="0" y="0" width="1200" height="600"/></clipPath>
    <linearGradient id="portraitTone" x1="0" y1="0" x2="0" y2="1">
      <stop offset="0" stop-color="#6b5a50"/>
      <stop offset=".35" stop-color="#3d4f6e"/>
      <stop offset="1" stop-color="#283a5c"/>
    </linearGradient>
  </defs>
  <g clip-path="url(#heroClip)">
    <circle cx="945" cy="484" r="305" fill="#e2e4e9"/>
    <path d="M0 595 H645" stroke="var(--blue-soft)" stroke-width="5" fill="none"/>
    <path d="M645 595 A323 323 0 1 1 1268 395" stroke="var(--blue-soft)" stroke-width="5" fill="none"/>
    <rect x="759" y="155" width="340" height="445" rx="120" fill="url(#portraitTone)" role="img" aria-label="Portrait photo of the contractor smiling with arms crossed"/>
  </g>
</svg>
<div class="abs greeting">Hi, I’m Name</div>
<h1 class="abs headline">An independent software contractor, architect &amp; tech trainer</h1>
<div class="abs btn btn-primary">Hire Me</div>
<div class="abs btn btn-outline">View Resume</div>

<!-- about -->
<section class="abs band" style="top:600px;height:255px"></section>
<h2 class="abs section-title" style="left:149px;top:651px">About Me</h2>
<div class="abs rule" style="left:149px;top:698px;width:157px"></div>
<p class="abs about-col" style="left:391px;top:664px">Lorem ipsum dolor sit amet, consectetur adipiscing elit. Ut urna justo, pellentesque a neque in, vulputate imperdiet erat. Donec sit amet finibus nisi. Donec enim lacus, dapibus mattis nibh a, auctor euismod odio.</p>
<p class="abs about-col" style="left:735px;top:664px">Vestibulum pharetra condimentum mi non molestie. Nullam blandit sodales mauris, condimentum interdum ante semper quis. Praesent feugiat, odio vel ullamcorper lacinia, dolor lorem venenatis metus, sed hendrerit arcu neque ac ex.</p>

<!-- services -->
<h2 class="abs section-title center" style="top:908px">Services</h2>
<div class="abs rule" style="left:533px;top:952px;width:133px"></div>
<p class="abs intro" style="top:967px">Nam est nisi, sagittis id purus sed, eleifend ultrices purus. Donec nibh<br>magna, congue quis vehicula quis, viverra a ipsum.</p>

<div class="abs card" style="left:149px">
  <svg viewBox="0 0 64 56" width="64" fill="none" stroke="var(--blue)" stroke-width="2"><rect x="2" y="2" width="60" height="38" rx="2"/><path d="M24 40l-3 10h22l-3-10M16 52h32"/><circle cx="24" cy="21" r="6"/><circle cx="41" cy="19" r="5"/></svg>
  <h3>Software Contracting</h3>
  <p>Sed condimentum commodo nulla a interdum. Morbi in fringilla mi. Praesent id tortor lacinia, viverra lectus id, rhoncus leo.</p>
</div>
<div class="abs card" style="left:457px">
  <svg viewBox="0 0 56 56" width="56" fill="none" stroke="var(--blue)" stroke-width="2"><path d="M12 18a12 12 0 0 1 24 0z"/><path d="M14 18v4a10 10 0 0 0 20 0v-4"/><path d="M4 54v-12a10 10 0 0 1 10-8h20a10 10 0 0 1 10 8v12"/><rect x="42" y="30" width="10" height="22" rx="2"/></svg>
  <h3>Architecture</h3>
  <p>Sed condimentum commodo nulla a interdum. Morbi in fringilla mi. Praesent id tortor lacinia, viverra lectus id, rhoncus leo.</p>
</div>
<div class="abs card" style="left:765px">
  <svg viewBox="0 0 60 56" width="60" fill="none" stroke="var(--blue)" stroke-width="2"><rect x="24" y="4" width="32" height="22"/><path d="M30 12h20M30 18h14"/><circle cx="10" cy="8" r="4"/><path d="M4 30v-10h12v10M6 30v14M14 30v14"/><circle cx="26" cy="38" r="3"/><circle cx="38" cy="38" r="3"/><circle cx="50" cy="38" r="3"/><path d="M20 50a6 6 0 0 1 12 0M32 50a6 6 0 0 1 12 0M44 50a6 6 0 0 1 12 0"/></svg>
  <h3>Tech Training</h3>
  <p>Sed condimentum commodo nulla a interdum. Morbi in fringilla mi. Praesent id tortor lacinia, viverra lectus id, rhoncus leo.</p>
</div>

<!-- skills -->
<section class="abs band" style="top:1372px;height:543px"></section>
<h2 class="abs section-title center" style="top:1424px">Skills</h2>
<div class="abs rule" style="left:559px;top:1470px;width:82px"></div>
<p class="abs intro" style="top:1483px">Nam est nisi, sagittis id purus sed, eleifend ultrices purus. Donec nibh<br>magna, congue quis vehicula quis, viverra a ipsum.</p>

<div class="abs skill" style="left:149px;top:1552px"><div class="skill-head"><span class="skill-name">Skill 1</span><span class="skill-pct">80%</span></div><div class="skill-track"><div class="skill-fill" style="width:80%"></div></div></div>
<div class="abs skill" style="left:149px;top:1635px"><div class="skill-head"><span class="skill-name">Skill 2</span><span class="skill-pct">75%</span></div><div class="skill-track"><div class="skill-fill" style="width:75%"></div></div></div>
<div class="abs skill" style="left:149px;top:1718px"><div class="skill-head"><span class="skill-name">Skill 3</span><span class="skill-pct">75%</span></div><div class="skill-track"><div class="skill-fill" style="width:75%"></div></div></div>
<div class="abs skill" style="left:149px;top:1800px"><div class="skill-head"><span class="skill-name">Skill 4</span><span class="skill-pct">90%</span></div><div class="skill-track"><div class="skill-fill" style="width:90%"></div></div></div>
<div class="abs skill" style="left:637px;top:1552px"><div class="skill-head"><span class="skill-name">Skill 5</span><span class="skill-pct">85%</span></div><div class="skill-track"><div class="skill-fill" style="width:85%"></div></div></div>
<div class="abs skill" style="left:637px;top:1635px"><div class="skill-head"><span class="skill-name">Skill 6</span><span class="skill-pct">80%</span></div><div class="skill-track"><div class="skill-fill" style="width:80%"></div></div></div>
<div class="abs skill" style="left:637px;top:1718px"><div class="skill-head"><span class="skill-name">Skill 7</span><span class="skill-pct">60%</span></div><div class="skill-track"><div class="skill-fill" style="width:60%"></div></div></div>
<div class="abs skill" style="left:637px;top:1800px"><div class="skill-head"><span class="skill-name">Skill 8</span><span class="skill-pct">90%</span></div><div class="skill-track"><div class="skill-fill" style="width:90%"></div></div></div>

<!-- experience -->
<h2 class="abs section-title center" style="top:1968px">Experience</h2>
<div class="abs rule" style="left:511px;top:2014px;width:178px"></div>
<p class="abs intro" style="top:2028px">Nam est nisi, sagittis id purus sed, eleifend ultrices purus. Donec nibh<br>magna, congue quis vehicula quis, viverra a ipsum.</p>
<div class="abs timeline-line"></div>

<div class="abs job-title" style="top:2110px">Your Position Title , Name of Company and Country</div>
<div class="abs job-dot" style="top:2118px"></div>
<div class="abs job-date" style="top:2151px">June 2018 - Present</div>
<p class="abs job-text" style="top:2111px">Lorem ipsum dolor sit amet, consectetur adipiscing elit. Ut urna justo, pellentesque a neque in, vulputate imperdiet erat. Donec sit amet finibus nisi.</p>

<div class="abs job-title" style="top:2252px">Your Position Title , Name of Company and Country</div>
<div class="abs job-dot" style="top:2260px"></div>
<div class="abs job-date" style="top:2293px">March 2016 - June 2018</div>
<p class="abs job-text" style="top:2253px">Lorem ipsum dolor sit amet, consectetur adipiscing elit. Ut urna justo, pellentesque a neque in, vulputate imperdiet erat. Donec sit amet finibus nisi.</p>

<div class="abs job-title" style="top:2392px">Your Position Title , Name of Company and Country</div>
<div class="abs job-dot" style="top:2400px"></div>
<div class="abs job-date" style="top:2433px">May 2013 - February 2016</div>
<p class="abs job-text" style="top:2393px">Lorem ipsum dolor sit amet, consectetur adipiscing elit. Ut urna justo, pellentesque a neque in, vulputate imperdiet erat. Donec sit amet finibus nisi.</p>

<div class="abs job-title" style="top:2531px">Your Position Title , Name of Company and Country</div>
<div class="abs job-dot" style="top:2539px"></div>
<div class="abs job-date" style="top:2572px">April 2011 - May 2013</div>
<p class="abs job-text" style="top:2532px">Lorem ipsum dolor sit amet, consectetur adipiscing elit. Ut urna justo, pellentesque a neque in, vulputate imperdiet erat. Donec sit amet finibus nisi.</p>

<!-- contact -->
<section class="abs band" style="top:2705px;height:585px"></section>
<h2 class="abs section-title" style="left:149px;top:2754px">Contact Me</h2>
<div class="abs rule" style="left:149px;top:2800px;width:184px"></div>
<p class="abs" style="left:149px;top:2815px;width:285px">Nam est nisi, sagittis id purus sed, eleifend ultrices purus. Donec nibh magna, congue quis vehicula quis, viverra a ipsum.</p>

<div class="abs contact-line" style="top:2933px">
  <svg viewBox="0 0 24 24"><path d="M12 1a8 8 0 0 0-8 8c0 6 8 14 8 14s8-8 8-14a8 8 0 0 0-8-8z" fill="#2b2b2b"/><circle cx="12" cy="9" r="3" fill="var(--band)"/></svg>
  <span>City, Country</span>
</div>
<div class="abs contact-line" style="top:2984px">
  <svg viewBox="0 0 24 24" fill="none" stroke="#2b2b2b" stroke-width="2"><path d="M5 3h4l2 5-3 2a11 11 0 0 0 6 6l2-3 5 2v4a2 2 0 0 1-2 2A18 18 0 0 1 3 5a2 2 0 0 1 2-2z"/></svg>
  <span>+11 2345 6789</span>
</div>
<div class="abs contact-line" style="top:3032px">
  <svg viewBox="0 0 24 24"><rect x="1" y="5" width="22" height="15" fill="#2b2b2b"/><path d="M1 5l11 9 11-9" fill="none" stroke="var(--band)" stroke-width="1.5"/></svg>
  <span>hello@samplemail.net</span>
</div>

<div class="abs form-panel"></div>
<div class="abs label" style="left:472px;top:2780px">Name</div>
<div class="abs label" style="left:757px;top:2780px">Email</div>
<div class="abs field" style="left:472px;top:2816px;width:271px;height:36px">Enter your name</div>
<div class="abs field" style="left:757px;top:2816px;width:271px;height:36px">Enter your email</div>
<div class="abs label" style="left:472px;top:2870px">Phone number</div>
<div class="abs label" style="left:757px;top:2870px">Service</div>
<div class="abs field" style="left:472px;top:2905px;width:271px;height:37px">Enter your phone number</div>
<div class="abs field" style="left:757px;top:2905px;width:271px;height:37px;justify-content:space-between">Pick a service
  <svg width="14" height="8" viewBox="0 0 14 8" fill="none" stroke="#666" stroke-width="1.5"><path d="M1 1l6 6 6-6"/></svg>
</div>
<div class="abs label" style="left:472px;top:2959px">Message</div>
<div class="abs field" style="left:472px;top:2994px;width:556px;height:151px;align-items:flex-start;padding-top:10px">Enter your message</div>
<div class="abs submit">Submit</div>

<!-- footer -->
<div class="abs footer-rule"></div>
<div class="abs socials">
  <span class="social"><i></i>Facenet</span>
  <span class="social"><i></i>Chirper</span>
  <span class="social"><i></i>Snapgram</span>
  <span class="social"><i></i>Worklink</span>
</div>
<div class="abs copyright">Website name 2020 © All Rights Reserved</div>

</body>
</html>
```